Logo + Label Design (Men’s Grooming Brand & Product Packaging)

Design a logo and 2 oz pomade label for Brant, a modern men’s grooming brand focused on clean, high-quality, natural ingredients. The design should establish a bold, masculine, minimalist identity that can later extend to products like shaving gel and body wash.

Key Requirements

Create a primary logo for “Brant” and a core label for the 2 oz pomade jar (screw-top).

Use a clean, modern style — masculine, confident, and approachable (think Wendel’s, Valto, Northfield Mill).

Design for 1–2 color screen printing on solid jar colors (white, black, or navy).

Avoid gradients, foil, or embossing. Must work in black & white.

Provide: vector logo, mockup of the 2 oz jar, color palette (CMYK/RGB/HEX), and font specs.

Winning design may lead to future projects (body wash, shave gel, skincare lines).

Font styles to use
Other font styles liked:
• We like the fonts and design concept in the attached mockup.

Requirements
Should not have
• We want to avoid too much writing or busy designs. We want to avoid having graphics/illustrations embedded in the logo if they will cause the brand to look less classy or sophisticated. We also want the design to look simple and all-American (e.g. Pellham and Stroud, Tall Pine, The BRIM, etc). We’d like to give a Kessler & Dunmore vibe that feels classy and high end.

```html
<!DOCTYPE html>
<html lang="en">
<head>
<meta charset="UTF-8">
<title>Brant Men's Hair Pomade – Label Design</title>
<link rel="stylesheet" href="https://fonts.googleapis.com/css2?family=Limelight&family=Poppins:wght@300;400;500;700&display=swap">
<style>
  :root {
    --ink: #161616;
    --paper: #ffffff;
    --soft-ink: #3a3a3a;
    --backdrop: #e9e9e7;
  }
  html, body {
    margin: 0;
    padding: 0;
    width: 1200px;
    height: 900px;
    overflow: hidden;
    background: var(--backdrop);
  }
  .canvas {
    position: relative;
    width: 1200px;
    height: 900px;
    display: flex;
    align-items: center;
    justify-content: space-around;
    padding: 0 40px;
    box-sizing: border-box;
  }
  .lid-label {
    width: 500px;
    height: 500px;
    display: block;
  }
  .lid-label .ring-text {
    font-family: "Poppins", sans-serif;
    font-weight: 500;
    font-size: 16.5px;
    fill: var(--paper);
    letter-spacing: 0.2px;
  }
  .lid-label .brand {
    font-family: "Poppins", sans-serif;
    font-weight: 700;
    font-size: 96px;
    fill: var(--ink);
    letter-spacing: -2px;
  }
  .lid-label .product {
    font-family: "Limelight", serif;
    font-size: 33px;
    fill: var(--ink);
  }
  .lid-label .scent {
    font-family: "Poppins", sans-serif;
    font-weight: 300;
    font-size: 25px;
    fill: var(--soft-ink);
  }
  .lid-label .hold {
    font-family: "Poppins", sans-serif;
    font-weight: 500;
    font-size: 22px;
    fill: var(--paper);
  }
  .lid-label .weight {
    font-family: "Poppins", sans-serif;
    font-weight: 400;
    font-size: 19px;
    fill: var(--ink);
  }

  .front-label {
    width: 480px;
    height: 380px;
    background: var(--paper);
    border-radius: 14px;
    display: flex;
    flex-direction: column;
    align-items: center;
    justify-content: center;
    box-sizing: border-box;
    padding: 30px 20px;
  }
  .front-label .brand {
    font-family: "Poppins", sans-serif;
    font-weight: 700;
    font-size: 76px;
    line-height: 1;
    color: var(--ink);
    letter-spacing: -2px;
    margin: 0 0 10px;
  }
  .front-label .product {
    font-family: "Limelight", serif;
    font-size: 34px;
    color: var(--ink);
    margin: 0;
    line-height: 1.1;
    white-space: nowrap;
  }
  .front-label .scent {
    font-family: "Poppins", sans-serif;
    font-weight: 300;
    font-size: 26px;
    color: var(--soft-ink);
    margin: 2px 0 4px;
  }
  .front-label .hold {
    font-family: "Poppins", sans-serif;
    font-weight: 500;
    font-size: 22px;
    color: var(--paper);
    background: var(--ink);
    width: 330px;
    text-align: center;
    padding: 3px 0;
    margin: 0 0 16px;
  }
  .front-label .weight {
    font-family: "Poppins", sans-serif;
    font-weight: 400;
    font-size: 19px;
    color: var(--ink);
    margin: 0;
  }
</style>
</head>
<body>
<main class="canvas">

  <svg class="lid-label" viewBox="0 0 520 520" xmlns="http://www.w3.org/2000/svg" aria-label="Lid label">
    <defs>
      <path id="ring-path" d="M260,493 A233,233 0 1 1 260,27 A233,233 0 1 1 260,493" fill="none"/>
      <clipPath id="inner-disc">
        <circle cx="260" cy="260" r="214"/>
      </clipPath>
    </defs>
    <circle cx="260" cy="260" r="258" fill="var(--ink)"/>
    <circle cx="260" cy="260" r="214" fill="var(--paper)"/>
    <text class="ring-text">
      <textPath href="#ring-path" startOffset="50%" text-anchor="middle">Naturally derived plant &amp; bee-based ingredients | Alcohol Free, Non-irritating | Formulated to minimize scalp irritation</textPath>
    </text>
    <text class="brand" x="260" y="178" text-anchor="middle">BRANT</text>
    <text class="product" x="260" y="238" text-anchor="middle">MENS HAIR POMADE</text>
    <text class="scent" x="260" y="278" text-anchor="middle">Fresh &amp; Clean</text>
    <g clip-path="url(#inner-disc)">
      <rect x="0" y="296" width="520" height="40" fill="var(--ink)"/>
    </g>
    <text class="hold" x="260" y="324" text-anchor="middle">Medium Hold - Matte Finish</text>
    <text class="weight" x="260" y="384" text-anchor="middle">NET WT 2 oz (57 g)</text>
  </svg>

  <section class="front-label" aria-label="Jar front label">
    <p class="brand">BRANT</p>
    <p class="product">MENS HAIR POMADE</p>
    <p class="scent">Fresh &amp; Clean</p>
    <p class="hold">Medium Hold – Matte Finish</p>
    <p class="weight">NET WT 2 oz (57 g)</p>
  </section>

</main>
</body>
</html>
```